Silver Fern Apothecary needs a label design or modification for new Kratom Co., need simple, eye catch

New company in Northern California that is going wholesale and retail for Kratom, a natural alternative from todays pharmaceutical drugs, we want to provide a better quality product than what the public in our area is generally exposed to, and eventually wider than Northern California

We need a better, eye catching, simple label design for our new Kratom line at Silver Fern Apothecary
This line will be Kratom that is harvested from the "Wild"....or "Forest Grown"
attached are files for capsule bottles, would like to be similar, but i don't feel the label "pops" or will grab enough attention.
It will be for Kratom ultra fine powder of premium grade, no stems and veins or any other additives or fillers

The existing Logo was created by pixel forge and would like it to be used
maybe with a graphic drawing of a Kratom leaf in the background ? not sure.
We are open to new ideas.

Maybe the label needs to be totally different, not sure.
Saw a friends project from pixel forge for Kratom, it was simple and i loved it, maybe even reduce the number of colors, maybe not
need the files in "AI" and would be nice if layered
there will be two different sizes
100g (3.527 oz) needs to be in the lower third of the bottom, in an area of
4 1/2" x 6"
50g (1.764 oz) in an area of 3 3/8" x 4"
The number declarations need to be at least 3/16" tall
as you will see from the attached files, some have green, red or white colors on the top and bottom of the label, this is to help the eye better catch the general type of strain for the customer and for the people selling the product
all other needed info will be in the attached files

The attached files are for Tortoise Kratom Tablets, the newer product is for Summit Kratom Blend (or maybe Select Kratom Blend), of various types.
Our product is better than most others and usually much stronger.
We provide consistency of product quality, which is hard to find with this item.

When printed "Silver Fern" doesnt stand out, especially with a black background, the black may make the printing of the gold darker than what it should be. Not sure if "Silver Fern" would be appropriate in white, or if i need a new design.

The Type of each kind may be added later simply because we carry so many different kinds, and as is said, we are open to new ideas.
Thank You

Target Market(s)

General public through wholesale to retailers, Kratom community

Industry/Entity Type

It Company

Font styles to use
Sans Serif
Other font styles liked:
• segoe print

Colors
fece3e
abd036
ec1f27
ffffff

Requirements
Must have
• size declarations of at least 3/16"
• and be taller than wide
Nice to have
• graphic picture of a Kratom leaf
Should not have
• for human consumption

```html
<!DOCTYPE html>
<html lang="en">
<head>
<meta charset="utf-8">
<title>Silver Fern Apothecary — Kratom Pouch Labels</title>
<link rel="stylesheet" href="https://fonts.googleapis.com/css2?family=Montserrat:wght@400;500;600;700&family=Mulish:wght@400;600&display=swap">
<style>
  :root {
    --bg: #eeeceb;
    --pouch: #ffffff;
    --pouch-shade: #f1f1f1;
    --seam: #e2e2e2;
    --ink: #2a2a2a;
    --ink-soft: #4a4a4a;
    --green: #1e9a45;
    --green-deep: #137a35;
    --red: #a8141e;
    --red-deep: #7e0c14;
    --black: #141414;
    --black-deep: #000000;
    --white: #ffffff;
  }
  * { box-sizing: border-box; margin: 0; padding: 0; }
  html, body { width: 1200px; height: 996px; overflow: hidden; }
  body {
    background: var(--bg);
    font-family: "Mulish", "Helvetica Neue", Arial, sans-serif;
    color: var(--ink);
  }
  .lineup {
    position: absolute;
    top: 292px;
    left: 165px;
    display: flex;
    gap: 24px;
  }
  .pouch {
    --accent: var(--green);
    --accent-deep: var(--green-deep);
    position: relative;
    width: 276px;
    height: 412px;
    background: linear-gradient(180deg, var(--pouch) 0%, var(--pouch) 60%, var(--pouch-shade) 100%);
    border-radius: 3px;
    overflow: hidden;
    box-shadow: 0 10px 24px rgba(0,0,0,0.14);
  }
  .pouch--red { --accent: var(--red); --accent-deep: var(--red-deep); }
  .pouch--white { --accent: var(--black); --accent-deep: var(--black-deep); }

  .pouch__zip {
    position: absolute;
    left: 0; right: 0;
    top: 42px;
    height: 2px;
    background: var(--seam);
  }
  .brand {
    position: absolute;
    top: 98px;
    left: 0; right: 0;
    display: flex;
    flex-direction: column;
    align-items: center;
    gap: 8px;
  }
  .brand__circle {
    width: 30px;
    height: 30px;
    border-radius: 50%;
    border: 2px solid var(--accent);
  }
  .brand__name {
    font-family: "Montserrat", Arial, sans-serif;
    font-weight: 600;
    font-size: 11px;
    letter-spacing: 0.08em;
    color: var(--ink);
    text-align: center;
    line-height: 1.35;
    text-transform: uppercase;
  }
  .product {
    position: absolute;
    top: 186px;
    left: 0; right: 0;
    text-align: center;
    font-family: "Montserrat", Arial, sans-serif;
    font-weight: 700;
    font-size: 35px;
    letter-spacing: 0.01em;
    color: var(--accent);
    line-height: 1;
  }
  .strain {
    position: absolute;
    top: 232px;
    left: 0; right: 0;
    text-align: center;
    font-size: 11.5px;
    color: var(--ink-soft);
  }
  .strain__type { color: var(--accent); font-weight: 600; }

  .claims {
    position: absolute;
    top: 277px;
    left: 0; right: 0;
    display: flex;
    justify-content: center;
    gap: 6px;
  }
  .claim {
    background: var(--accent);
    color: var(--white);
    font-size: 8px;
    font-weight: 600;
    letter-spacing: 0.02em;
    text-transform: uppercase;
    padding: 3px 10px;
    border-radius: 7px;
    line-height: 1.2;
  }
  .leaf-band {
    position: absolute;
    left: 0; right: 0;
    top: 300px;
    bottom: 0;
    background: linear-gradient(135deg, var(--accent) 0%, var(--accent-deep) 100%);
  }
  .net-weight {
    position: absolute;
    bottom: 10px;
    left: 50%;
    transform: translateX(-50%);
    background: rgba(0,0,0,0.35);
    color: var(--white);
    font-size: 9px;
    padding: 2px 8px;
    border-radius: 6px;
    white-space: nowrap;
  }
</style>
</head>
<body>
  <main class="lineup">
    <article class="pouch pouch--green">
      <div class="pouch__zip"></div>
      <div class="brand">
        <span class="brand__circle"></span>
        <span class="brand__name">Silver Fern<br>Apothecary</span>
      </div>
      <h2 class="product">KRATOM</h2>
      <p class="strain">Highland <span class="strain__type">Green</span> Heron</p>
      <div class="claims"><span class="claim">No Fillers</span><span class="claim">No Additives</span></div>
      <div class="leaf-band" role="img" aria-label="Pattern of translucent kratom leaf skeletons in green"></div>
      <span class="net-weight">100g (3.527 oz)</span>
    </article>

    <article class="pouch pouch--red">
      <div class="pouch__zip"></div>
      <div class="brand">
        <span class="brand__circle"></span>
        <span class="brand__name">Silver Fern<br>Apothecary</span>
      </div>
      <h2 class="product">KRATOM</h2>
      <p class="strain">Highland <span class="strain__type">Red</span> Heron</p>
      <div class="claims"><span class="claim">No Fillers</span><span class="claim">No Additives</span></div>
      <div class="leaf-band" role="img" aria-label="Pattern of translucent kratom leaf skeletons in red"></div>
      <span class="net-weight">100g (3.527 oz)</span>
    </article>

    <article class="pouch pouch--white">
      <div class="pouch__zip"></div>
      <div class="brand">
        <span class="brand__circle"></span>
        <span class="brand__name">Silver Fern<br>Apothecary</span>
      </div>
      <h2 class="product">KRATOM</h2>
      <p class="strain">Highland <span class="strain__type">White</span> Heron</p>
      <div class="claims"><span class="claim">No Fillers</span><span class="claim">No Additives</span></div>
      <div class="leaf-band" role="img" aria-label="Pattern of translucent kratom leaf skeletons in black and white"></div>
      <span class="net-weight">100g (3.527 oz)</span>
    </article>
  </main>
</body>
</html>
```